Walkthrough Splash Page for new Content Management Site

Clubnest.link is a new site that helps groups and individuals design a custom site, create content and manage their members.

Although we have already designed a solid "root" homepage (see attached), we would like a set of default pages for when a person creates a new site that will help guide them through customizing their Space and creating content.

The "Root" Homepage is found here:
https://www.clubnest.link

An example of the current "default space" (which is what we need designed) can be found here:
https://freshhub.clubnest.link/

About the Functionality
This is some of the functionality that we would like covered in the design:
- A Clubnest.link Space is composed of two components: the "Space" and the "Dashboard".
- The Dashboard is used to (1) create content (e.g. Events, Auctions, Articles, Newsletters, etc.), (2) design the Space (by creating Pages, customizing the Menu and modifying overall styles), (3) view analytics about the space (e.g. how many members have viewed the space or have purchased a ticket, and (4) change their profile.
- User's can also use their profile to login/register for any other Clubnest.link Space as well.
- In the Dashboard you will see a "Profile" section and an "Account" section. The "Account" section is the User's relationship with the current Space. The "Profile" section will be follow the user around to any space that they are logged into.
- As you will see in the Dashboard, alot of the functionality has not yet been implemented, but please create the default page as if it has already been completed (it is coming soon).

Required Pages
We need four pages designed for the default new space: homepage, membership, about and contact.

The most important page is the default homepage which will help provide an example of what the user's Space can look and provide instructions on how to use the site (with links to the places on the site where these things can take place).

The default site also has a default "Membership", page which is a good change to demo another design to entire new people to sign up for the new Space as well as a "About" and "Contact" page.

We encourage you to visit our site (https://www.clubnest.link) to get a feel for our current design, which is based on Sparrow Scaffold and Vela Panel (http://themecrate.net/preview/TC7702914). To see a site that has already been created and customized, see the Halvern College Graduates Society of New York (https://www.halvern-grads.club)

If you create a new Space you will see what the default page looks like (see attached).

I have also attached the Fonts, Icons and Color Palette that we currently use in the application - these are just to get you started, feel free to be creative!
Updates

Target Market(s)

Small groups, businesses and individuals who want to have an easy to way to create an online presence, especially those who wish to sell items online.

Industry/Entity Type

Management

Coding

Coded - Design and coding required

Number of Pages Required

4 page

Font styles to use
Serif
Other font styles liked:
• Kristie Sans (Attached)

Colors
3276b5
33a6d7

Requirements
Must have
• Clean, tactile, responsive UI with pictures and diagrams.
• The site site takes on a high-tech, social approach to content management, which should be reflected in the design.

```html
<!DOCTYPE html>
<html lang="en">
<head>
<meta charset="utf-8">
<title>Clubnest.link — Homepage</title>
<link href="https://fonts.googleapis.com/css2?family=Exo+2:wght@600;700&family=Ubuntu:ital,wght@0,400;0,500;0,700;1,400&display=swap" rel="stylesheet">
<style>
  :root{
    --brand:#3276b5;
    --sky:#33a6d7;
    --ink:#1f1f1f;
    --nav:#202020;
    --muted:#555;
    --card-line:#c9c9c9;
    --paper:#efefef;
    --white:#fff;
  }
  *{box-sizing:border-box;margin:0;padding:0}
  html,body{width:1200px;height:2247px;overflow:hidden}
  body{position:relative;background:var(--white);font-family:"Ubuntu",sans-serif;color:var(--ink)}
  .abs{position:absolute}

  /* header */
  .site-header{left:0;top:0;width:1200px;height:166px;background:var(--white);border-top:4px solid #2a2a2a}
  .brand{left:0;top:70px;width:1200px;display:flex;justify-content:center;align-items:center;gap:12px}
  .brand-dot{width:22px;height:22px;border-radius:50%;background:var(--brand)}
  .brand-name{font-weight:500;font-size:36px;color:#111;letter-spacing:.5px}
  .login{left:990px;top:132px;width:90px;height:34px;background:var(--brand);color:var(--white);font-size:15px;text-align:center;line-height:34px;border-radius:6px 6px 0 0}

  .main-nav{left:0;top:166px;width:1200px;height:43px;background:var(--nav)}
  .main-nav .site-name{left:128px;top:0;line-height:43px;color:#ddd;font-size:18px}
  .main-nav ul{right:112px;top:0;list-style:none;display:flex;gap:30px;line-height:43px;font-size:15px;color:#eee}
  .main-nav li.active{color:var(--sky)}

  /* hero */
  .hero{left:112px;top:218px;width:976px;height:261px;border:4px solid #e3e3e3;background:linear-gradient(90deg,#bfc4c9,#d9d4cd 25%,#c3cdd6 50%,#d7d0c8 75%,#b9c2cb)}
  .hero-panel{left:120px;top:70px;width:760px;height:108px;background:rgba(255,255,255,.88);display:flex;align-items:center;justify-content:center;text-align:center}
  .hero-panel p{font-style:italic;font-size:21px;line-height:31px;color:var(--brand);font-weight:500}

  /* features */
  .features{left:0;top:499px;width:1200px;height:887px;background:var(--paper)}
  .card{width:465px;height:112px}
  .card .box{left:-20px;top:50px;width:465px;height:80px;background:var(--white);border:1px solid var(--card-line);box-shadow:0 6px 8px -6px rgba(0,0,0,.35)}
  .card .hex{left:0;top:0;width:108px;height:112px}
  .card h3{left:130px;top:24px;font-family:"Exo 2",sans-serif;font-weight:700;font-size:22px;letter-spacing:1px;color:var(--brand)}
  .card p{left:130px;top:64px;width:320px;font-style:italic;font-size:14.5px;line-height:23px;color:var(--muted)}

  /* content band */
  .content-band{left:0;top:1386px;width:1200px;height:385px;background:linear-gradient(90deg,#5fc6f2,#7dd3f6 55%,#9bdcf6)}
  .members-band{left:0;top:1771px;width:1200px;height:442px;background:linear-gradient(90deg,#151515,#3a3a3a 45%,#1b1b1b)}
  .laptop{border-radius:6px;background:linear-gradient(180deg,#1a1a1a 0,#1a1a1a 4%,#f4f4f4 4%,#f4f4f4 86%,#c9ccd0 86%,#e9eaec 92%,#9aa0a6 100%)}
  .band-title{font-family:"Exo 2",sans-serif;font-weight:700;font-size:25px;letter-spacing:1px}
  .band-copy{font-style:italic;font-size:17px;line-height:27px}

  .cta{left:128px;top:2117px;width:944px;height:67px;background:var(--brand)}
  .cta p{left:22px;top:0;line-height:67px;color:var(--white);font-style:italic;font-size:21px}
  .cta .button{left:729px;top:9px;width:200px;height:49px;background:var(--sky);color:var(--white);font-family:"Exo 2",sans-serif;font-weight:700;font-size:20px;text-align:center;line-height:49px;letter-spacing:.5px}

  .site-footer{left:0;top:2213px;width:1200px;height:34px;background:#0c0c0c;color:#8a8a8a;font-size:12px;text-align:center;line-height:34px}
</style>
</head>
<body>
<svg width="0" height="0" class="abs">
  <defs>
    <filter id="hexShadow" x="-20%" y="-20%" width="140%" height="150%"><feDropShadow dx="0" dy="3" stdDeviation="3" flood-opacity=".25"/></filter>
    <symbol id="hexFrame" viewBox="0 0 108 112"><polygon points="27,8 81,8 106,56 81,104 27,104 2,56" fill="#fff" stroke="#3276b5" stroke-width="3.5" filter="url(#hexShadow)"/></symbol>
  </defs>
</svg>

<header class="abs site-header">
  <div class="abs brand"><span class="brand-dot"></span><span class="brand-name">Clubnest.link</span></div>
  <div class="abs login">LOGIN</div>
</header>

<nav class="abs main-nav">
  <div class="abs site-name">Clubnest.link</div>
  <ul class="abs"><li class="active">HOMEPAGE</li><li>MEMBERSHIP</li><li>ABOUT</li><li>CONTACT</li></ul>
</nav>

<section class="abs hero" role="img" aria-label="Collage of portrait photos of members and professionals">
  <div class="abs hero-panel"><p>Clubnest.link helps groups or individuals design a custom site, create content<br>and manage their members.</p></div>
</section>

<section class="abs features">
  <!-- row 1 -->
  <div class="abs card" style="left:144px;top:31px">
    <div class="abs box"></div>
    <svg class="abs hex" viewBox="0 0 108 112"><use href="#hexFrame"/><g fill="none" stroke="#3276b5" stroke-width="3"><circle cx="54" cy="56" r="17" fill="#3276b5"/><path d="M40 50q14 6 28 0M40 62q14-6 28 0M54 39q-9 17 0 34" stroke="#fff" stroke-width="2.5"/></g></svg>
    <h3 class="abs">SPACES</h3><p class="abs">Create a customizable Space to manage Members and content.</p>
  </div>
  <div class="abs card" style="left:629px;top:31px">
    <div class="abs box"></div>
    <svg class="abs hex" viewBox="0 0 108 112"><use href="#hexFrame"/><g fill="#3276b5"><circle cx="54" cy="50" r="13"/><circle cx="43" cy="38" r="6"/><circle cx="65" cy="38" r="6"/><rect x="42" y="58" width="24" height="16" rx="8"/></g></svg>
    <h3 class="abs">COMMERCE</h3><p class="abs">Easily create an e-commerce site to sell your products.</p>
  </div>
  <!-- row 2 -->
  <div class="abs card" style="left:144px;top:198px">
    <div class="abs box"></div>
    <svg class="abs hex" viewBox="0 0 108 112"><use href="#hexFrame"/><g fill="#3276b5"><rect x="47" y="36" width="14" height="24" rx="7"/><path d="M42 54q0 14 12 14t12-14" fill="none" stroke="#3276b5" stroke-width="3"/><rect x="52" y="68" width="4" height="8"/><rect x="45" y="75" width="18" height="3"/></g></svg>
    <h3 class="abs">NEWSLETTERS</h3><p class="abs">Manage contacts and newsletters to reach your Members.</p>
  </div>
  <div class="abs card" style="left:629px;top:198px">
    <div class="abs box"></div>
    <svg class="abs hex" viewBox="0 0 108 112"><use href="#hexFrame"/><g fill="#3276b5"><rect x="34" y="42" width="40" height="28" rx="3"/><circle cx="45" cy="53" r="5" fill="#fff"/><rect x="40" y="60" width="10" height="5" fill="#fff"/><rect x="55" y="50" width="14" height="3" fill="#fff"/><rect x="55" y="56" width="14" height="3" fill="#fff"/><rect x="55" y="62" width="10" height="3" fill="#fff"/></g></svg>
    <h3 class="abs">MEMBERSHIPS</h3><p class="abs">Manage Members with paid or free Membership Levels.</p>
  </div>
  <!-- row 3 -->
  <div class="abs card" style="left:144px;top:366px">
    <div class="abs box"></div>
    <svg class="abs hex" viewBox="0 0 108 112"><use href="#hexFrame"/><g fill="#3276b5"><rect x="40" y="36" width="28" height="40" rx="2"/><g fill="#fff"><rect x="45" y="42" width="6" height="6"/><rect x="54" y="43" width="10" height="3"/><rect x="45" y="52" width="19" height="3"/><rect x="45" y="58" width="19" height="3"/><rect x="45" y="64" width="13" height="3"/></g></g></svg>
    <h3 class="abs">INVOICES</h3><p class="abs">Request ad hoc payments for a product or service from anyone.</p>
  </div>
  <div class="abs card" style="left:629px;top:366px">
    <div class="abs box"></div>
    <svg class="abs hex" viewBox="0 0 108 112"><use href="#hexFrame"/><g fill="#3276b5"><rect x="44" y="36" width="22" height="12" rx="2" transform="rotate(-40 55 42)"/><rect x="51" y="46" width="5" height="30" rx="2" transform="rotate(-40 53 61)"/><rect x="36" y="72" width="22" height="5" rx="1"/></g></svg>
    <h3 class="abs">AUCTIONS</h3><p class="abs">Manage donors, lots and bids.</p>
  </div>
  <!-- row 4 -->
  <div class="abs card" style="left:144px;top:535px">
    <div class="abs box"></div>
    <svg class="abs hex" viewBox="0 0 108 112"><use href="#hexFrame"/><g fill="#3276b5"><rect x="34" y="42" width="40" height="28" rx="2"/><g fill="#fff"><rect x="38" y="46" width="14" height="10"/><rect x="55" y="46" width="15" height="3"/><rect x="55" y="52" width="15" height="3"/><rect x="38" y="60" width="32" height="3"/></g></g></svg>
    <h3 class="abs">ARTICLES</h3><p class="abs">Create blog posts with advanced formatting and social commenting.</p>
  </div>
  <div class="abs card" style="left:629px;top:535px">
    <div class="abs box"></div>
    <svg class="abs hex" viewBox="0 0 108 112"><use href="#hexFrame"/><g fill="#3276b5"><rect x="38" y="38" width="24" height="8" rx="3"/><rect x="38" y="48" width="24" height="8" rx="3"/><rect x="38" y="58" width="24" height="8" rx="3"/><circle cx="64" cy="64" r="11"/><circle cx="64" cy="64" r="6" fill="#fff"/></g></svg>
    <h3 class="abs">BUDGETS</h3><p class="abs">Create budgets for events and issue reimbursements to organizers.</p>
  </div>
  <!-- row 5 -->
  <div class="abs card" style="left:144px;top:703px">
    <div class="abs box"></div>
    <svg class="abs hex" viewBox="0 0 108 112"><use href="#hexFrame"/><g fill="#3276b5"><rect x="36" y="38" width="36" height="36" rx="3"/><rect x="40" y="46" width="28" height="24" fill="#fff"/><polygon points="54,50 57,56 63,57 58,61 59,67 54,64 49,67 50,61 45,57 51,56"/></g></svg>
    <h3 class="abs">EVENTS</h3><p class="abs">Create events and sell tickets from a consolidated interface.</p>
  </div>
  <div class="abs card" style="left:629px;top:703px">
    <div class="abs box"></div>
    <svg class="abs hex" viewBox="0 0 108 112"><use href="#hexFrame"/><path d="M54 76 36 58a11 11 0 0 1 18-14 11 11 0 0 1 18 14z" fill="#3276b5"/></svg>
    <h3 class="abs">FUNDRAISERS</h3><p class="abs">Accept donations and allow donors to specify an earmark.</p>
  </div>
</section>

<section class="abs content-band" role="img" aria-label="Soft blue workspace backdrop with a laptop">
  <div class="abs laptop" style="left:135px;top:52px;width:438px;height:272px" role="img" aria-label="Laptop showing the events dashboard"></div>
  <h2 class="abs band-title" style="left:562px;top:130px;color:#2c3e50">CREAT CONTENT</h2>
  <p class="abs band-copy" style="left:570px;top:172px;color:#1f4f6e">Create a variety of free and paid content from a unified interface.<br>Create a variety of free and paid content from a unified interface.</p>
</section>

<section class="abs members-band" role="img" aria-label="Dark backdrop of hands arranging member blocks">
  <h2 class="abs band-title" style="left:395px;top:118px;color:#8b8b8b">MANAGE MEMBERS</h2>
  <p class="abs band-copy" style="left:146px;top:155px;color:#9a9a9a">Create a variety of free and paid content from a unified interface.<br>Create a variety of free and paid content from a unified interface.</p>
  <div class="abs laptop" style="left:636px;top:37px;width:454px;height:272px" role="img" aria-label="Laptop showing the events dashboard"></div>
</section>

<div class="abs cta">
  <p class="abs">Clubnest.link is provide you to make your own site with some simple steps...</p>
  <div class="abs button">CREAT YOUR SITE</div>
</div>

<footer class="abs site-footer">Powered by Clubnest.link</footer>
</body>
</html>
```